Kirevoli Tea & Dairy Farm Website

Design a mainly visual informational website incorporating examples uploaded of a tea and dairy farm in Africa. I can provide more pictures.

I do take suggestions willing.

Industry/Entity Type

Farm

Font styles to use
Serif

Colors
acd037

```html
<!DOCTYPE html>
<html lang="en">
<head>
<meta charset="utf-8">
<title>Kirevoli Tea &amp; Dairy Farm</title>
<link rel="stylesheet" href="https://fonts.googleapis.com/css2?family=Playfair+Display:wght@400;700&family=Lato:wght@400;700&display=swap">
<style>
:root{
  --green-dark:#2f5b1c;
  --green:#3f7424;
  --lime:#acd037;
  --ink:#333;
  --muted:#666;
  --grey-band:#ececec;
  --footer:#3b3b3b;
  --white:#fff;
}
*{margin:0;padding:0;box-sizing:border-box}
html,body{width:1200px;height:2272px;overflow:hidden;background:var(--white)}
body{font-family:"Lato",Arial,sans-serif;color:var(--ink);font-size:12px;line-height:1.6}
.wrap{width:864px;margin:0 auto;position:relative}

/* header */
.site-header{height:44px}
.site-header .wrap{height:44px;display:flex;align-items:center;justify-content:space-between}
.brand{display:flex;align-items:center;gap:8px}
.brand-mark{width:12px;height:12px;background:var(--ink)}
.brand-name{font-family:"Lato",Arial,sans-serif;font-weight:700;font-size:17px;color:var(--ink);line-height:1}
.header-contact{display:flex;align-items:center;gap:8px;font-size:11px;color:var(--muted)}
.header-contact svg{width:13px;height:13px}
.main-nav{background:var(--green-dark);height:20px}
.main-nav ul{list-style:none;display:flex;gap:26px;height:20px;align-items:center}
.main-nav a{color:var(--white);font-size:9px;font-weight:700;text-decoration:none;letter-spacing:.5px}

/* hero */
.hero{height:408px;position:relative;background:linear-gradient(180deg,#5d7d4a 0%,#3f6431 45%,#233f1c 100%)}
.hero-text{position:absolute;left:168px;top:196px;color:var(--white);width:430px}
.hero-text h1{font-family:"Playfair Display",Georgia,serif;font-size:24px;line-height:1.25;letter-spacing:1px;font-weight:700}
.hero-text p{font-size:10px;margin:14px 0 16px;color:#eef}
.btn{display:inline-block;background:var(--green-dark);color:var(--white);font-size:9px;font-weight:700;padding:5px 14px;letter-spacing:.5px;text-decoration:none}
.hero-arrow{position:absolute;top:186px;width:28px;height:28px;border-radius:50%;background:rgba(0,0,0,.35);display:flex;align-items:center;justify-content:center}
.hero-arrow.prev{left:40px}.hero-arrow.next{right:40px}

/* sections */
.section-title{font-family:"Playfair Display",Georgia,serif;color:var(--green-dark);font-size:21px;text-align:center;font-weight:700;letter-spacing:1px;line-height:1.3}
.section-intro{text-align:center;width:700px;margin:8px auto 0;color:var(--muted);font-size:10px}

.services{height:348px;padding-top:84px}
.service-grid{display:flex;gap:16px;margin-top:28px}
.service-card{width:160px}
.service-photo{height:100px}
.card-bar{display:flex;justify-content:space-between;align-items:center;padding:5px 0;font-size:9px;color:var(--muted)}
.card-bar .more{background:var(--green-dark);color:var(--white);padding:1px 8px;font-size:8px}

.occasions{background:var(--grey-band);height:340px;padding-top:50px}
.occasion-grid{display:flex;gap:16px;margin-top:26px}
.occasion-card{width:204px}
.occasion-photo{height:150px}

.features{height:340px;padding-top:88px}
.feature-grid{display:flex;gap:26px}
.feature{width:270px}
.feature-photo{height:72px;position:relative}
.feature-photo .tag{position:absolute;left:10px;bottom:-8px;background:var(--green-dark);color:var(--white);font-size:8px;padding:1px 8px}
.feature h3{font-size:10px;font-weight:700;margin:16px 0 4px;color:var(--ink);letter-spacing:.5px}
.feature p{font-size:10px;color:var(--muted)}

.videos{height:532px}
.videos .wrap{display:flex;gap:36px;padding-top:60px}
.video-frame{width:400px;height:260px;position:relative}
.video-play{position:absolute;left:50%;top:50%;transform:translate(-50%,-50%)}
.video-copy{flex:1}
.video-copy h2{font-family:"Playfair Display",Georgia,serif;color:var(--green-dark);font-size:21px;font-weight:700;letter-spacing:1px;margin-bottom:6px;line-height:1.3}
.video-copy p{font-size:10px;color:var(--muted);margin-bottom:8px}

.buzz{background:var(--green-dark);height:168px;color:var(--white);position:relative;padding-top:12px}
.buzz-title{font-family:"Playfair Display",Georgia,serif;font-size:20px;font-weight:700;text-align:center;letter-spacing:1px;line-height:1.3}
.buzz-body{display:flex;gap:26px;width:740px;margin:12px auto 0;align-items:flex-start}
.buzz-avatar{width:80px;height:80px;border-radius:50%;background:linear-gradient(160deg,#d6d9dc,#8c949c);flex:none;border:3px solid var(--white)}
.buzz-name{font-weight:700;font-size:12px;line-height:1.4}
.buzz-date{font-size:9px;color:#cfe0c2;margin-bottom:4px}
.buzz-quote{font-size:10px;color:#e6efe0}
.quote-mark{position:absolute;font-family:"Playfair Display",Georgia,serif;font-size:34px;color:rgba(255,255,255,.5);line-height:1}
.buzz-arrow{position:absolute;top:84px;font-size:18px;color:rgba(255,255,255,.7)}

.site-footer{background:var(--footer);height:72px;color:#ccc}
.site-footer .wrap{display:flex;justify-content:space-between;align-items:center;height:72px}
.footer-nav{list-style:none;display:flex;gap:16px;font-size:9px}
.footer-copy{font-size:8px;color:#999;margin-top:4px}
.socials{display:flex;gap:6px}
.socials span{width:16px;height:16px;border-radius:50%;background:#888;display:block}
</style>
</head>
<body>

<header class="site-header">
  <div class="wrap">
    <div class="brand">
      <span class="brand-mark"></span>
      <span class="brand-name">Kirevoli Tea &amp; Dairy Farm</span>
    </div>
    <div class="header-contact">
      <svg viewBox="0 0 24 24"><path fill="#2f5b1c" d="M6.6 10.8a15 15 0 0 0 6.6 6.6l2.2-2.2a1 1 0 0 1 1-.25 11 11 0 0 0 3.6.6 1 1 0 0 1 1 1V20a1 1 0 0 1-1 1A17 17 0 0 1 3 4a1 1 0 0 1 1-1h3.5a1 1 0 0 1 1 1c0 1.25.2 2.45.6 3.6a1 1 0 0 1-.25 1z"/></svg>
      <span>Call Us : +256 700 418 902</span>
    </div>
  </div>
</header>

<nav class="main-nav">
  <div class="wrap">
    <ul>
      <li><a href="#">ABOUT</a></li><li><a href="#">BLOG</a></li><li><a href="#">TEA</a></li><li><a href="#">DAIRY</a></li><li><a href="#">INFRASTRUCTURE</a></li><li><a href="#">RETREAT</a></li><li><a href="#">TIME SHARE</a></li><li><a href="#">SENIOR LIVING</a></li><li><a href="#">CONTACT</a></li>
    </ul>
  </div>
</nav>

<section class="hero" role="img" aria-label="Farmhouse on a hill above green tea fields">
  <div class="hero-arrow prev"><svg width="12" height="12" viewBox="0 0 12 12"><path d="M8 1 3 6l5 5" stroke="#fff" stroke-width="2" fill="none"/></svg></div>
  <div class="hero-arrow next"><svg width="12" height="12" viewBox="0 0 12 12"><path d="m4 1 5 5-5 5" stroke="#fff" stroke-width="2" fill="none"/></svg></div>
  <div class="hero-text">
    <h1>WELCOME TO<br>KIREVOLI TEA &amp; DAIRY FARM</h1>
    <p>Set among green hills, our estate grows fine tea and keeps a healthy dairy herd. We welcome guests, partners and families to walk the fields, taste fresh produce and share in the life of a working farm.</p>
    <a class="btn" href="#">READ MORE</a>
  </div>
</section>

<section class="services">
  <div class="wrap">
    <h2 class="section-title">OUR SERVICES</h2>
    <p class="section-intro">From tea picking to milk processing, our teams look after every step with care. Explore the services we offer to visitors, buyers and the families who live and work on the farm.</p>
    <div class="service-grid">
      <div class="service-card"><div class="service-photo" role="img" aria-label="Tea pickers in the field" style="background:linear-gradient(#9bb07a,#4d6a32)"></div><div class="card-bar"><span>Services - 01</span><span class="more">Read More</span></div></div>
      <div class="service-card"><div class="service-photo" role="img" aria-label="Dairy cows in a shed" style="background:linear-gradient(#d8d4c8,#6e6a5e)"></div><div class="card-bar"><span>Services - 02</span><span class="more">Read More</span></div></div>
      <div class="service-card"><div class="service-photo" role="img" aria-label="Cattle on open pasture" style="background:linear-gradient(#b9c9a3,#5b6b3c)"></div><div class="card-bar"><span>Services - 03</span><span class="more">Read More</span></div></div>
      <div class="service-card"><div class="service-photo" role="img" aria-label="Farm buildings and grounds" style="background:linear-gradient(#a9b7a0,#4b5a3e)"></div><div class="card-bar"><span>Services - 04</span><span class="more">Read More</span></div></div>
      <div class="service-card"><div class="service-photo" role="img" aria-label="Solar panels on the estate" style="background:linear-gradient(#c9d3dc,#56606a)"></div><div class="card-bar"><span>Services - 05</span><span class="more">Read More</span></div></div>
    </div>
  </div>
</section>

<section class="occasions">
  <div class="wrap">
    <h2 class="section-title">SPECIAL OCCASIONS</h2>
    <div class="occasion-grid">
      <div class="occasion-card"><div class="occasion-photo" role="img" aria-label="Wedding party gathering outdoors" style="background:linear-gradient(#c98a7a,#6b3a34)"></div><div class="card-bar"><span>Occasions - 01</span><span class="more">Read More</span></div></div>
      <div class="occasion-card"><div class="occasion-photo" role="img" aria-label="Celebration with guests in bright dress" style="background:linear-gradient(#c86a5a,#5a2e2a)"></div><div class="card-bar"><span>Occasions - 02</span><span class="more">Read More</span></div></div>
      <div class="occasion-card"><div class="occasion-photo" role="img" aria-label="Decorated reception tables" style="background:linear-gradient(#d6c6b4,#7a5e48)"></div><div class="card-bar"><span>Occasions - 03</span><span class="more">Read More</span></div></div>
      <div class="occasion-card"><div class="occasion-photo" role="img" aria-label="Garden event on the lawn" style="background:linear-gradient(#8fae6a,#3f5a2a)"></div><div class="card-bar"><span>Occasions - 04</span><span class="more">Read More</span></div></div>
    </div>
  </div>
</section>

<section class="features">
  <div class="wrap feature-grid">
    <article class="feature">
      <div class="feature-photo" role="img" aria-label="Supplier portrait in an office" style="background:linear-gradient(#c7ccd2,#4f5660)"><span class="tag">Read More</span></div>
      <h3>SUPPLIERS</h3>
      <p>Partner with us to supply seedlings, feed and equipment. We value fair terms, steady orders and long working ties with local traders.</p>
    </article>
    <article class="feature">
      <div class="feature-photo" role="img" aria-label="Job listing board" style="background:linear-gradient(#e2b0a2,#a0463a)"><span class="tag">Read More</span></div>
      <h3>JOBS</h3>
      <p>Join a growing team in the fields, the dairy and the guest house. We train new staff and open roles through the whole season.</p>
    </article>
    <article class="feature">
      <div class="feature-photo" role="img" aria-label="Young plant held in open hands" style="background:linear-gradient(#cfe0b4,#5e7f3a)"><span class="tag">Read More</span></div>
      <h3>INVESTORS</h3>
      <p>Invest in a farm with a clear plan for growth. Our board shares regular reports on yields, herd health and new projects.</p>
    </article>
  </div>
</section>

<section class="videos">
  <div class="wrap">
    <div class="video-frame" role="img" aria-label="Video still of a speaker at the farm" style="background:linear-gradient(135deg,#b8a58c,#5a4a3a)">
      <svg class="video-play" width="50" height="50" viewBox="0 0 50 50"><circle cx="25" cy="25" r="24" fill="rgba(0,0,0,.45)"/><path d="M20 15 36 25 20 35z" fill="#fff"/></svg>
    </div>
    <div class="video-copy">
      <h2>VIDEOS</h2>
      <p>Watch short films about daily life on the estate, from the first morning pick to evening milking. Each clip shows how our people care for the land, the herd and the guests who visit.</p>
      <p>Our latest series follows the new processing line, the retreat cottages and the school garden project run with nearby families.</p>
      <p>New videos are added each month, so come back often to see the seasons change.</p>
      <a class="btn" href="#">VIEW ALL VIDEOS</a>
    </div>
  </div>
</section>

<section class="buzz">
  <h2 class="buzz-title">BUZZ</h2>
  <span class="quote-mark" style="left:330px;top:48px">&ldquo;</span>
  <span class="quote-mark" style="right:210px;top:128px">&rdquo;</span>
  <span class="buzz-arrow" style="left:180px">&#8249;</span>
  <span class="buzz-arrow" style="right:180px">&#8250;</span>
  <div class="buzz-body">
    <div class="buzz-avatar" role="img" aria-label="Portrait of the reviewer"></div>
    <div>
      <div class="buzz-name">Daniel Okello</div>
      <div class="buzz-date">Posted on 27 March 2014</div>
      <p class="buzz-quote">A wonderful stay. The tea tour was the best part of our trip, the staff were kind and the fresh milk and bread each morning were a treat. We walked the hills, met the pickers and left with gifts for the whole family. We will be back next year.</p>
    </div>
  </div>
</section>

<footer class="site-footer">
  <div class="wrap">
    <div>
      <ul class="footer-nav"><li>ABOUT</li><li>BLOG</li><li>TEA</li><li>DAIRY</li><li>INFRASTRUCTURE</li><li>RETREAT</li><li>TIME SHARE</li><li>SENIOR LIVING</li><li>CONTACT</li></ul>
      <div class="footer-copy">COPYRIGHT &copy; 2014 KIREVOLI TEA &amp; DAIRY FARM. ALL RIGHTS RESERVED.</div>
    </div>
    <div class="socials"><span></span><span></span><span></span><span></span><span></span></div>
  </div>
</footer>

</body>
</html>
```